dsadasdasdasdsa

Industry/Entity Type

Mortgage Broking

Requirements
Must have
• Call-to-action button somewhere on the graphic
Nice to have
• The font of our logo is Montserrat

```html
<!DOCTYPE html>
<html lang="en">
<head>
<meta charset="utf-8">
<title>Need a Mortgage Broker? Banner</title>
<link href="https://fonts.googleapis.com/css2?family=Jost:wght@500;600;700&family=Quicksand:wght@400;500;600;700&display=swap" rel="stylesheet">
<style>
  :root {
    --green: #1a7444;
    --green-bright: #2eac6d;
    --rust: #6b2014;
    --white: #ffffff;
    --ink: #222222;
    --muted: #666666;
    --line: #dddddd;
    --panel: #f5f5f5;
    --stage: #f1f1f1;
    --turtle-light: #6fbf4a;
    --turtle-dark: #2f8a4f;
    --shell: #8a4a25;
    --sky: #6fb3e8;
    --house: #a8aa96;
  }
  * { box-sizing: border-box; margin: 0; padding: 0; }
  html, body { width: 1200px; height: 957px; overflow: hidden; background: var(--white); }
  body { position: relative; font-family: "Quicksand", sans-serif; color: var(--ink); }

  .stage-fade {
    position: absolute; left: 0; top: 330px; width: 1200px; height: 627px;
    background: linear-gradient(180deg, var(--white) 0%, var(--stage) 40%, #e9e9e9 100%);
  }

  /* Banner */
  .banner { position: absolute; background: var(--green); overflow: hidden; }
  .banner-large { left: 24px; top: 148px; width: 1140px; height: 166px; }
  .banner-small { left: 28px; top: 50px; width: 673px; height: 97px; }
  .mascot {
    position: absolute; bottom: 0;
    background: radial-gradient(ellipse at 50% 35%, var(--turtle-light) 0%, var(--turtle-dark) 55%, var(--shell) 100%);
    border-radius: 45% 45% 0 0;
  }
  .banner-large .mascot-left { left: 4px; width: 220px; height: 160px; }
  .banner-large .mascot-right { right: 36px; width: 170px; height: 162px; }
  .banner-small .mascot-left { left: 2px; width: 128px; height: 94px; }
  .banner-small .mascot-right { right: 20px; width: 100px; height: 95px; }
  .banner-heading {
    position: absolute; left: 0; right: 0; text-align: center;
    font-family: "Jost", sans-serif; font-weight: 700; color: var(--white); white-space: nowrap;
  }
  .banner-large .banner-heading { top: 21px; font-size: 43px; line-height: 43px; letter-spacing: 2.4px; padding-left: 12px; }
  .banner-small .banner-heading { top: 13px; font-size: 25px; line-height: 25px; letter-spacing: 1.4px; padding-left: 12px; }
  .banner-cta {
    position: absolute; background: var(--rust); color: var(--white);
    font-family: "Jost", sans-serif; font-weight: 500; text-align: center; white-space: nowrap;
  }
  .banner-large .banner-cta { left: 260px; top: 78px; width: 642px; height: 55px; line-height: 55px; border-radius: 8px; font-size: 21px; letter-spacing: 3.4px; }
  .banner-small .banner-cta { left: 154px; top: 46px; width: 379px; height: 31px; line-height: 31px; border-radius: 4px; font-size: 12.5px; letter-spacing: 1.9px; }

  /* Web page */
  .web-page {
    position: absolute; left: 99px; top: 452px; width: 991px; height: 520px;
    background: var(--white); box-shadow: 0 6px 30px rgba(0,0,0,0.18);
  }
  .main-nav { position: absolute; left: 27px; top: 0; height: 30px; display: flex; }
  .nav-item {
    height: 30px; line-height: 30px; text-align: center;
    font-size: 11px; font-weight: 700; color: var(--ink); border-right: 1px solid #e6e6e6;
  }
  .nav-item:last-child { border-right: none; }
  .caret { font-size: 8px; margin-left: 4px; }

  .util-links { position: absolute; top: 42px; left: 759px; display: flex; align-items: center; font-size: 11px; font-weight: 500; }
  .util-links span { margin-right: 12px; }
  .btn-brokers {
    background: var(--green); color: var(--white); font-size: 9.5px; font-weight: 700;
    width: 67px; height: 22px; line-height: 22px; text-align: center; border-radius: 3px;
  }
  .quick-search { position: absolute; left: 767px; top: 77px; display: flex; height: 19px; }
  .qs-icon { width: 26px; border: 1px solid #ccc; border-radius: 3px 0 0 3px; display: flex; align-items: center; justify-content: center; }
  .qs-input { width: 96px; border: 1px solid #ccc; border-left: none; font-size: 7.5px; color: #999; line-height: 17px; padding-left: 6px; white-space: nowrap; overflow: hidden; }
  .qs-button { margin-left: 4px; width: 39px; background: var(--green); color: var(--white); font-size: 8px; font-weight: 700; text-align: center; line-height: 19px; border-radius: 2px; }

  .breadcrumb { position: absolute; left: 30px; top: 157px; font-size: 8.5px; font-weight: 500; }
  .breadcrumb .sep { color: #bbb; margin: 0 4px; }

  .post-meta {
    position: absolute; left: 28px; top: 189px; width: 673px; height: 28px;
    background: var(--panel); border: 1px solid var(--line); border-radius: 3px;
    font-size: 8px; line-height: 26px; padding: 0 6px; color: var(--muted);
  }
  .post-meta .category { color: var(--green); font-weight: 600; }
  .post-meta .print { position: absolute; right: 12px; top: 0; color: var(--ink); display: flex; align-items: center; gap: 3px; height: 26px; }

  .post-title { position: absolute; left: 28px; top: 230px; font-size: 19px; line-height: 24px; font-weight: 500; color: var(--ink); }
  .title-rule { position: absolute; left: 28px; top: 265px; width: 673px; height: 1px; background: var(--line); }

  .post-image { position: absolute; left: 28px; top: 279px; width: 673px; height: 260px; background: #d4d4d4; }
  .post-photo {
    position: absolute; left: 128px; top: 0; width: 418px; height: 260px;
    background: linear-gradient(180deg, var(--sky) 0%, #a9d2f0 30%, var(--house) 60%, #8b8e7c 100%);
  }

  .search-panel {
    position: absolute; left: 721px; top: 189px; width: 211px; height: 195px;
    border: 1px solid var(--line); border-radius: 4px; background: var(--white);
    box-shadow: 0 2px 8px rgba(0,0,0,0.12); padding: 14px 13px;
  }
  .field-label { font-size: 9.5px; line-height: 12px; font-weight: 700; margin-bottom: 4px; }
  .field {
    width: 184px; height: 21px; border: 1px solid #ccc; border-radius: 3px;
    font-size: 8.5px; color: #999; line-height: 19px; padding-left: 8px; margin-bottom: 12px; position: relative;
  }
  .field .drop { position: absolute; right: 6px; top: 0; font-size: 6px; color: #555; }
  .btn-search {
    width: 184px; height: 22px; background: var(--green-bright); color: var(--white);
    font-size: 9.5px; font-weight: 600; text-align: center; line-height: 22px; border-radius: 3px; margin-top: -1px;
  }
</style>
</head>
<body>
  <div class="stage-fade"></div>

  <section class="banner banner-large">
    <div class="mascot mascot-left" role="img" aria-label="Cartoon turtle mascot smiling"></div>
    <div class="mascot mascot-right" role="img" aria-label="Cartoon turtle mascot pointing"></div>
    <h1 class="banner-heading">Need a Mortgage Broker?</h1>
    <div class="banner-cta">Search Now on Australia's Largest Directory</div>
  </section>

  <div class="web-page">
    <nav class="main-nav">
      <div class="nav-item" style="width:170px">Home</div>
      <div class="nav-item" style="width:186px">Directory<span class="caret">&#8964;</span></div>
      <div class="nav-item" style="width:175px">Instant Broker Match</div>
      <div class="nav-item" style="width:191px">Resources<span class="caret">&#8964;</span></div>
      <div class="nav-item" style="width:168px">Add Your Business<span class="caret">&#8964;</span></div>
    </nav>

    <section class="banner banner-small">
      <div class="mascot mascot-left" role="img" aria-label="Cartoon turtle mascot smiling"></div>
      <div class="mascot mascot-right" role="img" aria-label="Cartoon turtle mascot pointing"></div>
      <div class="banner-heading">Need a Mortgage Broker?</div>
      <div class="banner-cta">Search Now on Australia's Largest Directory</div>
    </section>

    <div class="util-links">
      <span>Contact Us</span><span>Login</span>
      <div class="btn-brokers">For Brokers</div>
    </div>
    <div class="quick-search">
      <div class="qs-icon">
        <svg width="8" height="8" viewBox="0 0 10 10"><circle cx="4" cy="4" r="3" fill="none" stroke="#333" stroke-width="1.5"/><line x1="6.3" y1="6.3" x2="9.3" y2="9.3" stroke="#333" stroke-width="1.5"/></svg>
      </div>
      <div class="qs-input">Start Typing Broker's N</div>
      <div class="qs-button">Search</div>
    </div>

    <div class="breadcrumb">Home<span class="sep">/</span>Blog<span class="sep">/</span>How to Find a Good Mortgage Broker?</div>

    <div class="post-meta">Posted 06/02/2024 in <span class="category">Using a Mortgage Broker</span>
      <span class="print">
        <svg width="8" height="7" viewBox="0 0 8 7"><rect x="2" y="0" width="4" height="2" fill="#333"/><rect x="0" y="2" width="8" height="3" rx="0.5" fill="#333"/><rect x="2" y="4" width="4" height="3" fill="#fff" stroke="#333" stroke-width="0.8"/></svg>Print
      </span>
    </div>
    <h2 class="post-title">How to Find a Good Mortgage Broker?</h2>
    <div class="title-rule"></div>
    <div class="post-image">
      <div class="post-photo" role="img" aria-label="Photo of a suburban house with a broker standing in front"></div>
    </div>

    <aside class="search-panel">
      <div class="field-label">Select Search Category:</div>
      <div class="field">Select Sub-Category<span class="drop">&#9660;</span></div>
      <div class="field-label">Specializing in:</div>
      <div class="field">Specializing in:<span class="drop">&#9660;</span></div>
      <div class="field-label">Location</div>
      <div class="field">Search City Name for Best Results</div>
      <div class="btn-search">Search Now</div>
    </aside>
  </div>
</body>
</html>
```